Update Annual Report Layout in IN-Design

This job is to create an In-Design layout for an annual report based on the style of previous versions of the annual reports and the exisiting style guide, but they also want to incorporate some new graphic elements they have used in the "Quick Reference Guide May 2019" document attached. Document Specs: The paper size is B5, approx. 80 pages including cover, CMYK. Style direction: Reference documents are attached. The new report design is expected to be similar in size, content and layout, however they would like the design to be more consistent with new design elements they have started using in the Quick Reference Guide May 2019 and in the 2019-20 corporate plan (attached). Deliverables: By Tuesday September 17 We need 1 set of the layouts listed below (with dummy text). 1 x Cover (front and back) 1 x internal single page layout - (all text) 1 x internal single page layout - (text and image) 1 x internal single page layout - (image only) 1 x internal 2 page spread layout - (all text) 1 x internal 2 page spread layout - (text and image) 1 x internal 2 page spread layout - (image only) 1 x Internal single page placeholder page for where the financial documents will be added. Once the client has provided feedback on the initial mock-ups, we will get you to make any requested edits and create a shell document for our typesetter. We also have a range of collateral and digital assets be made using this branding, so if this initial engagement goes well there is definitely the potential for immediate additional work. Regards Darvel

Target Market(s)

Government Annual report

Industry/Entity Type

Government

Font styles to use
Serif
Sans Serif

Colors
9bcb3c
f78f20
6b449b
f04a51
faa54b
3176b5

Requirements
Must have
• Document Specs: paper size is B5, CMYK.
Nice to have
• The new report design is expected to be similar in size, content and layout, however they would like the design to be more consistent with new design elements they have started using in the Quick Reference Guide May 2019 and in the 2019-20 corporate plan (attached).

```html
<!DOCTYPE html>
<html lang="en">
<head>
<meta charset="utf-8">
<title>PTRA Annual Report 2019–20 — Part 1 Overview</title>
<link href="https://fonts.googleapis.com/css2?family=Nunito+Sans:wght@400;700;800;900&family=Montserrat:wght@800&family=Libre+Baskerville:ital,wght@1,700&display=swap" rel="stylesheet">
<style>
  :root{
    --green:#9bcb3c;
    --orange:#f78f20;
    --purple:#6b449b;
    --red:#f04a51;
    --amber:#faa54b;
    --blue:#3176b5;
    --sky:#2f8fe0;
    --ink:#1d1d1b;
    --paper:#ffffff;
  }
  *{box-sizing:border-box;margin:0;padding:0}
  html,body{width:1200px;height:852px;overflow:hidden;background:var(--paper)}
  body{font-family:"Nunito Sans",Arial,sans-serif;color:var(--ink);position:relative}
  .spread{position:relative;width:1200px;height:852px}
  .page{position:absolute;top:0;height:852px;width:600px}
  .page--left{left:0}
  .page--right{left:604px}

  .running-head{position:absolute;top:34px;height:27px;display:flex}
  .running-head svg{display:block}
  .running-head .title{position:absolute;left:17px;top:6px;color:#fff;font-size:9.2px;letter-spacing:.01em;white-space:nowrap}
  .running-head .section{position:absolute;top:6px;color:var(--ink);font-size:9.4px;font-weight:800;white-space:nowrap}

  .col{position:absolute;font-size:11.2px;line-height:13.1px}
  .col p{margin-bottom:13.1px}
  .col ul{list-style:none;margin-bottom:6px}
  .col ul li{position:relative;padding-left:13.5px}
  .col ul li::before{content:"";position:absolute;left:1px;top:4px;width:4px;height:5px;background:var(--green);clip-path:polygon(50% 0,100% 50%,50% 100%,0 50%)}
  .col ol{list-style:none;margin-bottom:13.1px;padding-left:7px}
  .col ol li span{color:var(--orange);display:inline-block;width:13px}

  .section-tab{position:absolute;height:27px;color:#fff;font-family:"Montserrat",sans-serif;font-weight:800;font-size:13.2px;letter-spacing:.02em;line-height:27px;padding-left:15px;background:var(--green);clip-path:polygon(0 0,95% 0,100% 50%,95% 100%,0 100%,4% 50%)}

  .photo{position:absolute;border-radius:50%}
  .photo--staff-portrait{left:931px;top:87px;width:160px;height:160px;background:radial-gradient(circle at 45% 40%,#e7a0b8,#b0647c 55%,#5a3a2c)}
  .photo--staff-celebration{left:929px;top:243px;width:130px;height:130px;background:radial-gradient(circle at 50% 45%,#c44a52,#7b4a3a 55%,#86a855)}
  .photo--birthday-cake{left:1028px;top:217px;width:110px;height:110px;border:4px solid #fff;background:radial-gradient(circle at 50% 50%,#f3eee2,#d8d0c0 60%,#b9c6a4)}
  .photo--leaders{left:673px;top:649px;width:141px;height:141px;background:radial-gradient(circle at 50% 55%,#5b8f3a,#3a3a3e 55%,#9aa3a6)}
  .caption{position:absolute;left:812px;top:658px;font-size:8px;font-weight:800;line-height:10.2px;letter-spacing:.02em}

  .footer-chevrons{position:absolute;top:831px;left:0}
  .folio{position:absolute;top:823px;width:46px;height:28px}
  .folio span{position:absolute;left:0;top:3px;width:42px;text-align:center;font-family:"Libre Baskerville",serif;font-style:italic;font-weight:700;font-size:13px}
</style>
</head>
<body>
<div class="spread">

  <!-- LEFT PAGE -->
  <section class="page page--left">
    <header class="running-head" style="left:34px">
      <svg width="495" height="27" viewBox="0 0 495 27">
        <polygon points="0,0 368,0 374,13.5 368,27 0,27 6,13.5" fill="var(--sky)"/>
        <polygon points="372,0 489,0 495,13.5 489,27 372,27 378,13.5" fill="var(--amber)"/>
      </svg>
      <span class="title">PARLIAMENTARY TRAVEL REVIEW AUTHORITY ANNUAL REPORT 2019–20</span>
      <span class="section" style="left:390px">PART 1 &nbsp;&gt;&nbsp; OVERVIEW</span>
    </header>

    <div class="col" style="left:69px;top:73px;width:228px">
      <p>Under the new framework, PTRA provides advice to parliamentarians to help them claim travel expenditure in line with the legislated principles in the PBR Act. We provide personal advice, Travel Advice Certificates, and post-travel rulings. In addition, in 2018–19 we will continue to deliver guidance and educational activities for parliamentarians and their staff on the new framework.</p>
      <p>There has already been much work undertaken to help stakeholders transition to the new framework:</p>
      <ul>
        <li>Information sessions – frequently held across Australia to inform parliamentarians and their staff of PTRA’s role and functions, and to discuss the new principles-based framework.</li>
        <li>Regular meetings with parliamentarians – since the commencement of the new framework, I have met with parliamentarians, the Usher of the Black Rod and the Serjeant-at-Arms. The PTRA Executive and staff continue to meet with parliamentarians and their staff as required.</li>
        <li>Providing responsive and high quality personal advice - PTRA logged, 11,494 individual client contacts during 2017–18 with 97 per cent having had a response within the agreed 24 hour timeframe.</li>
      </ul>
    </div>

    <h2 class="section-tab" style="left:54px;top:511px;width:211px">Governance arrangements</h2>
    <div class="col" style="left:69px;top:544px;width:228px">
      <p>I have really enjoyed working with the Members of the Authority who are responsible for PTRA’s statutory functions. The Members were appointed by the Governor-General and each Member brings specialist skills and experience to PTRA.</p>
      <p>The Members met eight times in 2017–18 to provide PTRA with strategic guidance on issues such as the performance of our functions.</p>
      <p>We have also established an Audit and Risk Committee to provide me with independent assurance on PTRA’s financial and performance reporting responsibilities, risk oversight and management, and system of internal control. This Committee met four times during 2017–18.</p>
    </div>

    <h2 class="section-tab" style="left:296px;top:66px;width:151px">Establishing PTRA</h2>
    <div class="col" style="left:311px;top:99px;width:226px">
      <p>Since commencing as CEO, I have focused on establishing a transparent, service-oriented and collaborative culture within PTRA. As a new organisation with high-profile clients, it is important to both embed and translate the culture from theory to practice. Our approach includes regular ‘curious conversations’ sessions, where staff are asked to consider an ethical dilemma related to their work, and associated legislative and compliance obligations.</p>
      <p>In line with the broader APS agenda, our agency seeks to continuously improve its operations. We continue to look at what improvements can be made in our operational environment through the establishment of four employee working groups. These groups include:</p>
      <ol>
        <li><span>1.</span>Staff and culture</li>
        <li><span>2.</span>Communication and education</li>
        <li><span>3.</span>Posterity and privacy</li>
        <li><span>4.</span>Risk, security and integrity.</li>
      </ol>
      <p>In April, we held a planning day and each of the working groups presented their recommendations as to how we could continue to maintain a great culture, communicate openly and strategically, and consider our legal obligations and risks.</p>
      <p>These working groups are helping PTRA to be more inclusive and insightful. Supporting staff to contribute to decisions that affect them is a priority for PTRA and our rates of participation show how effective our approach has been:</p>
      <ul>
        <li>For the 2018 APS Census, 96.4 per cent of staff completed the survey, which was the second highest response rate for small agencies in the APS.</li>
        <li>PTRA sits in third place in comparison to the overall APS index score in the 2018 APS Census with regard to innovation.</li>
        <li>The positive vote for the 2018–2021 PTRA Enterprise Agreement saw a high engagement level with 94.6 per cent of staff voting.</li>
        <li>The Staff and Culture working group established a PTRA social club,</li>
      </ul>
    </div>

    <svg class="footer-chevrons" width="250" height="27" viewBox="0 0 250 27" aria-hidden="true">
      <polygon points="0,0 35,0 44,13.5 35,27 0,27" fill="var(--purple)"/>
      <polygon points="40,0 76,0 85,13.5 76,27 40,27 49,13.5" fill="var(--sky)"/>
      <polygon points="81,0 117,0 126,13.5 117,27 81,27 90,13.5" fill="var(--green)"/>
      <polygon points="122,0 158,0 167,13.5 158,27 122,27 131,13.5" fill="var(--amber)"/>
      <polygon points="163,0 199,0 208,13.5 199,27 163,27 172,13.5" fill="var(--orange)"/>
      <polygon points="204,0 240,0 249,13.5 240,27 204,27 213,13.5" fill="var(--red)"/>
    </svg>
    <div class="folio" style="left:525px">
      <svg width="46" height="28" viewBox="0 0 46 28"><polygon points="1,1 36,1 44,14 36,27 1,27 8,14" fill="none" stroke="var(--green)" stroke-width="1.3"/></svg>
      <span>1</span>
    </div>
  </section>

  <!-- RIGHT PAGE -->
  <section class="page page--right">
    <header class="running-head" style="left:35px">
      <svg width="495" height="27" viewBox="0 0 495 27">
        <polygon points="0,0 368,0 374,13.5 368,27 0,27 6,13.5" fill="var(--sky)"/>
        <polygon points="372,0 489,0 495,13.5 489,27 372,27 378,13.5" fill="var(--amber)"/>
      </svg>
      <span class="title">PARLIAMENTARY TRAVEL REVIEW AUTHORITY ANNUAL REPORT 2019–20</span>
      <span class="section" style="left:390px">PART 1 &nbsp;&gt;&nbsp; OVERVIEW</span>
    </header>
  </section>

  <div class="col" style="left:686px;top:73px;width:230px">
    <p>coordinating events for Harmony Day and ANZAC Day, and raising money for the Hartwell Family Foundation.</p>
  </div>

  <h2 class="section-tab" style="left:661px;top:130px;width:150px">External relations</h2>
  <div class="col" style="left:673px;top:164px;width:228px">
    <p>I have made a concerted effort to meet with parliamentarians to advise them of their obligations and provide advice on applying the legislated principles to their travel arrangements.</p>
    <p>I initially endeavoured to meet with the members of the Senate Standing Committees on Finance and Public Administration, and have since met with many other parliamentarians who were directly affected by changes under the new framework.</p>
    <p>In March, I presented at an International Integrity Council (IIC) conference on the link between an impartial merit-based public sector and public integrity.</p>
    <p>I also participated on an expert panel at IIC Global Integrity and Trust Forum. For this forum I was asked to contribute to a session on ‘Ethical Superhumans? Behavioural Insights for Integrity.’ This participation allowed me to share ideas and lessons learnt with other jurisdictions about supporting and developing cultural change, and building trust in institutions.</p>
    <p>The IIC conference and forum was an important opportunity to introduce PTRA to the international community. A significant outcome of my participation</p>
  </div>

  <div class="photo photo--staff-portrait" role="img" aria-label="Photo of a smiling staff member in a checked shirt"></div>
  <div class="photo photo--staff-celebration" role="img" aria-label="Photo of a staff member enjoying the birthday celebration"></div>
  <div class="photo photo--birthday-cake" role="img" aria-label="Photo of a decorated birthday cake for the Authority"></div>

  <div class="col" style="left:915px;top:400px;width:228px">
    <p>was agreement by the IIC to help Australia create a network of other countries and interested parties in the area of parliamentary expenses.</p>
    <p>I visited the Legislative Standards Office (LSO) in the United Kingdom and met with its CEO, Mr Edmund Rooke. Following this, PTRA and LSO have established regular teleconferences between relevant senior officers to exchange ideas and experiences on issues of mutual interest.</p>
    <p>In May, I met with officials from the Eastern State Department of Premier and Cabinet who are in the process of setting up an independent Remuneration Tribunal to determine salary and allowances for State Members of Parliament and senior public sector executives. They were particularly interested in hearing about PTRA’s advisory and review work.</p>
    <p>By 30 June 2018, we had achieved all of our performance targets, highlighting the dedication and professionalism of PTRA staff.</p>
  </div>

  <div class="photo photo--leaders" role="img" aria-label="Photo of the LSO CEO and the PTRA CEO standing together"></div>
  <p class="caption">LSO CEO Edmund<br>Rooke with PTRA CEO<br>Conan Darvel</p>

  <svg class="footer-chevrons" style="left:604px" width="250" height="27" viewBox="0 0 250 27" aria-hidden="true">
    <polygon points="0,0 35,0 44,13.5 35,27 0,27 9,13.5" fill="var(--purple)"/>
    <polygon points="40,0 76,0 85,13.5 76,27 40,27 49,13.5" fill="var(--sky)"/>
    <polygon points="81,0 117,0 126,13.5 117,27 81,27 90,13.5" fill="var(--green)"/>
    <polygon points="122,0 158,0 167,13.5 158,27 122,27 131,13.5" fill="var(--amber)"/>
    <polygon points="163,0 199,0 208,13.5 199,27 163,27 172,13.5" fill="var(--orange)"/>
    <polygon points="204,0 240,0 249,13.5 240,27 204,27 213,13.5" fill="var(--red)"/>
  </svg>
  <div class="folio" style="left:1128px">
    <svg width="46" height="28" viewBox="0 0 46 28"><polygon points="1,1 36,1 44,14 36,27 1,27 8,14" fill="none" stroke="var(--green)" stroke-width="1.3"/></svg>
    <span>2</span>
  </div>

</div>
</body>
</html>
```